Velmora Intergrated Marketing Stationary Design Contest

We require a very professional looking stationary set to include: letterhead, compliments slip and business cards (double sided bus cards).

Files should be supplied on either Illustrator or InDesign.

We are interested in perhaps encorporating a faint watermark with the letter q or the logo, but it isnt a pre-requisite

Target Market(s)

Business owners seeking professional marketing services

Industry/Entity Type

Marketing

Requirements
Must have
• Concurrent theme wiht business cards, letterhead and comp slip. Must be an editable document for future ammendment
Should not have
• No use of times new roman or similar fonts

```html
<!DOCTYPE html>
<html lang="en">
<head>
<meta charset="utf-8">
<title>Velmora Integrated Marketing – Letterhead</title>
<link href="https://fonts.googleapis.com/css2?family=Nunito+Sans:wght@300;400&display=swap" rel="stylesheet">
<style>
  :root {
    --brand-orange: #f05a28;
    --ink: #3c3c3c;
    --ink-soft: #8a8a8a;
    --paper: #ffffff;
  }
  * { margin: 0; padding: 0; box-sizing: border-box; }
  html, body { width: 848px; height: 1200px; overflow: hidden; background: var(--paper); }
  .letterhead {
    position: relative;
    width: 848px;
    height: 1200px;
    overflow: hidden;
    background: var(--paper);
    font-family: "Nunito Sans", Arial, sans-serif;
    color: var(--ink);
  }
  .accent-shapes { position: absolute; inset: 0; }
  .brand {
    position: absolute;
    top: 134px;
    right: 36px;
    display: flex;
    align-items: center;
    gap: 12px;
  }
  .brand-dot {
    width: 40px; height: 40px;
    border-radius: 50%;
    background: var(--brand-orange);
  }
  .brand-name {
    font-size: 34px;
    font-weight: 300;
    letter-spacing: 4px;
    color: #1e1e1e;
    line-height: 1;
  }
  .sender {
    position: absolute;
    left: 51px;
    top: 1008px;
    font-weight: 300;
  }
  .sender-name { font-size: 14.5px; color: var(--ink); line-height: 18px; }
  .sender-tagline { font-size: 11.5px; color: var(--brand-orange); line-height: 18px; margin-bottom: 2px; }
  .sender-details { font-size: 11.5px; line-height: 16px; color: var(--ink); }
  .sender-details .label { color: var(--brand-orange); }
  .legal {
    position: absolute;
    left: 51px;
    top: 1174px;
    display: flex;
    gap: 22px;
    font-size: 9px;
    font-weight: 300;
    color: var(--ink-soft);
  }
</style>
</head>
<body>
<div class="letterhead">
  <svg class="accent-shapes" width="848" height="1200" viewBox="0 0 848 1200" aria-hidden="true">
    <circle class="accent-top" cx="-14" cy="156" r="112" fill="var(--brand-orange)"/>
    <ellipse class="accent-bottom" cx="752" cy="1040" rx="178" ry="168" fill="var(--brand-orange)"/>
  </svg>

  <div class="brand">
    <span class="brand-dot"></span>
    <span class="brand-name">velmora</span>
  </div>

  <address class="sender" style="font-style: normal;">
    <p class="sender-name">Velmora Intergrated Marketing</p>
    <p class="sender-tagline">Tag line here</p>
    <div class="sender-details">
      <p>Harbour House</p>
      <p>Marlow Row, Brindley</p>
      <p>North Ashdale, BR14 7QN</p>
      <p><span class="label">w:</span> www.velmoraim.co.uk</p>
      <p><span class="label">e:</span> enquiries@velmoraim.co.uk</p>
      <p><span class="label">t:</span> 01632 960418</p>
      <p><span class="label">f:</span> 01632 960427</p>
    </div>
  </address>

  <div class="legal">
    <span>Company registration 4817305</span>
    <span>Vat No 582 1047 36</span>
    <span>Trading as a division of Brantwick Ltd</span>
  </div>
</div>
</body>
</html>
```